Label Sticker Design for Apothecary Brand

Hello! We are an independent grassroots business located in Ontario, Canada that specializes in making organic botanical and herbal skin care, tea, witchcraft and wellness products. We have been in business for 5 years and are looking to create a label sticker with one of our slogans for use in packaging.

Our brand is dark, herbal, witchy, and modern with old-world apothecary and vintage influences. We want a label that will be VERY clean, and easily explain what our product is, while conveying a sense of mysticism and magic, as well as a traditional apothecary vibe.

We have attached design inspiration to give you an idea of the style that we would like. Our demographic is hipster, current, (think finger tattoos, linen dresses, and organic groceries), and they care deeply about where we source our ingredients, and how we craft our product. We don't want an old-school sticker that looks like it should be on the shelves of a health food store. The design should be contemporary, upmarket, modern and clean, but evoke a strong sense of magic and self-care with wild gathered herbs and unusual wild flowers!

This will be used as a packaging sticker for our shipping boxes.

We look forward to your winning design!
Thank you very much.

Target Market(s)

20 - 50yr Female Demographic
Natural, bohemian, earthy, hipster and modern

Key Words: Minimalist Tattoos, Organic Skin Care, Bohemian, Witchy, Dark, Moody, Confident, Sustainable, Ethical,

PLEASE VIEW PHOTOS BEFORE SUBMITTING A DESIGN ;)

Industry/Entity Type

Skin Care Product

Font styles to use
Serif
Script

Colors
1b1b1b
5c5c5c
fbfbfb

Requirements
Must have
• Clean and Simple - Take a look at the photos we've posted!
• Black / greyscale (No color)
• Label sticker must be a rectangle (3" x 2")
• Very Modern with a touch of old-world
• We are open to a variety of font styles. Please see photo FONT in image files, or the images 'Bottle Inspiration'
• Please use the following text:
• Thornmoor Stillhouse
• --------------------
• Crafted with Magic
• * Once your design is chosen and purchased, we will require the names of all fonts and sources of imagery used.
Nice to have
• A moody botanical graphic surrounding the text. Tangled wild, antique botanical illustrations. Not mandatory, but would be very nice.
Should not have
• Colour
• Messy or overly dramatic fonts
• Cartoon Imagery
• Leaf Motif
• Female Body Silhouettes
• Scroll or decorative borders.
• Butterflies, birds etc
• Actual pictures of witches
• Mandalas or Messy Graphics

```html
<!DOCTYPE html>
<html lang="en">
<head>
<meta charset="utf-8">
<title>Thornmoor Stillhouse – Rose and Chamomile Honey Clay Cleanser Label</title>
<link rel="stylesheet" href="https://fonts.googleapis.com/css2?family=Oswald:wght@300&display=swap">
<style>
  :root {
    --ink: #000000;
    --paper: #fbfbfb;
    --charcoal: #1b1b1b;
    --slate: #5c5c5c;
    --mist: #9a9a9a;
  }
  html, body {
    margin: 0;
    padding: 0;
    width: 1200px;
    height: 800px;
    overflow: hidden;
    background: var(--ink);
  }
  .label {
    position: relative;
    width: 1200px;
    height: 800px;
    background: var(--ink);
    font-family: "Oswald", "Arial Narrow", sans-serif;
    font-weight: 300;
    color: var(--charcoal);
  }
  .label__art {
    position: absolute;
    left: 0;
    top: 0;
  }
  .label__text {
    position: absolute;
    left: 0;
    width: 1200px;
    margin: 0;
    text-align: center;
    white-space: nowrap;
  }
  .brand-name {
    top: 338px;
    font-size: 50px;
    line-height: 58px;
    letter-spacing: 1px;
    color: var(--ink);
  }
  .product-name {
    top: 542px;
    font-size: 31px;
    line-height: 46px;
    color: var(--charcoal);
  }
  .slogan {
    top: 661px;
    font-size: 20px;
    line-height: 26px;
    letter-spacing: 2px;
    color: var(--charcoal);
  }
  .net-weight {
    top: 755px;
    font-size: 20px;
    line-height: 26px;
    letter-spacing: 1px;
    color: var(--paper);
  }
</style>
</head>
<body>
<main class="label">
  <svg class="label__art" width="1200" height="800" viewBox="0 0 1200 800">
    <defs>
      <radialGradient id="bouquetTone" cx="0.5" cy="0.45" r="0.6">
        <stop offset="0" stop-color="#8a8a8a"/>
        <stop offset="0.6" stop-color="#5c5c5c"/>
        <stop offset="1" stop-color="#2a2a2a"/>
      </radialGradient>
    </defs>
    <path class="bouquet" role="img"
          aria-label="Engraved antique botanical bouquet of peonies, buds and wild foliage in white line art, gathered around the top of the label"
          fill="url(#bouquetTone)"
          d="M300 300 C300 250 340 240 380 250 C390 200 420 170 470 180 C480 130 500 60 560 55 C610 55 620 110 600 140 C640 120 680 110 700 130 C730 150 740 200 760 220 C790 230 830 290 870 310 C890 360 880 420 860 480 C840 520 810 530 800 500 C760 440 700 420 600 410 C500 420 430 460 400 530 C380 540 330 520 320 470 C300 420 290 350 300 300 Z"/>
    <circle class="seal" cx="600" cy="511" r="223" fill="var(--paper)"/>
    <circle class="seal__ring" cx="600" cy="511" r="212" fill="none" stroke="var(--ink)" stroke-width="2"/>
    <line class="divider" x1="493" y1="520" x2="713" y2="520" stroke="var(--ink)" stroke-width="1.5"/>
    <line class="divider" x1="487" y1="656" x2="716" y2="656" stroke="var(--ink)" stroke-width="1.5"/>
  </svg>

  <h1 class="label__text brand-name">Thornmoor<br>Stillhouse</h1>
  <p class="label__text product-name">Rose and Chamomile<br>Honey Clay Cleanser</p>
  <p class="label__text slogan">Crafted with Magic</p>
  <p class="label__text net-weight">80g</p>
</main>
</body>
</html>
```